Vela Stewardship Business Card design

We need a creative business card design for our hospitality management company
We need the following information:
Our business Logo: Vela Stewardship
Name: Mara Dobrinsky
Phone number: 0458 317 642
Email: mara@velastewardship.com.au
Address: 214/53 Penrose Street, South Melbourne 3206
Web: www.velastewardship.com.au
I need the design to be a working file so that I can insert the names and numbers of the other staff members of our business.
The cards need to be 90 x 40mm
Thanks
Industry/Entity Type
Hospitality
Look and feel

```html
<!DOCTYPE html>
<html lang="en">
<head>
<meta charset="utf-8">
<title>Vela Stewardship – Business Card Options</title>
<link rel="stylesheet" href="https://fonts.googleapis.com/css2?family=Oswald:wght@600&family=Open+Sans:wght@400;600&display=swap">
<style>
  :root {
    --stage: #5b3b27;
    --orange: #f39a1e;
    --orange-light: #f8b93a;
    --yellow: #fdbd18;
    --yellow-deep: #f7a612;
    --ink: #222222;
    --card-white: #f4f4f4;
    --card-grey-top: #ffffff;
    --slate: #48484c;
    --charcoal: #3f3f43;
    --umber: #4e433d;
    --label: #ffffff;
    --watermark: rgba(0,0,0,0.06);
  }
  * { margin: 0; padding: 0; box-sizing: border-box; }
  html, body { width: 1200px; height: 620px; overflow: hidden; }
  body {
    position: relative;
    background: var(--stage);
    font-family: "Open Sans", Arial, sans-serif;
  }
  .card {
    position: absolute;
    width: 546px;
    height: 242px;
    box-shadow: 0 4px 10px rgba(0,0,0,0.45);
    overflow: hidden;
  }
  .card--front   { left: 39px;  top: 58px;  background: linear-gradient(180deg, var(--card-grey-top), #ececec); }
  .card--white   { left: 600px; top: 58px;  background: linear-gradient(100deg, #e6e6e6, var(--card-grey-top) 50%, #e2e2e2); }
  .card--slate   { left: 39px;  top: 318px; height: 240px; background: var(--charcoal); }
  .card--umber   { left: 600px; top: 318px; height: 240px; background: var(--umber); }

  .brand-mark {
    position: absolute;
    width: 96px; height: 88px;
    background: linear-gradient(160deg, var(--orange-light), var(--orange));
  }
  .brand-name {
    position: absolute;
    font-family: "Oswald", "Arial Narrow", sans-serif;
    font-weight: 600;
    text-transform: uppercase;
    color: var(--orange);
    white-space: nowrap;
    letter-spacing: 0.5px;
  }

  /* front */
  .card--front .brand-mark { left: 129px; top: 24px; }
  .card--front .brand-name { left: 31px; top: 118px; font-size: 32px; }
  .contact {
    position: absolute;
    right: 30px; top: 22px;
    text-align: right;
    font-size: 12.5px;
    line-height: 16px;
    color: var(--ink);
  }
  .contact-line::after {
    content: "";
    display: inline-block;
    width: 7px; height: 7px;
    margin-left: 6px;
    border-radius: 50%;
    background: var(--orange);
    vertical-align: middle;
  }
  .watermark-square {
    position: absolute;
    left: 419px; top: 92px;
    width: 80px; height: 80px;
    background: var(--watermark);
  }
  .address-band {
    position: absolute;
    left: 0; top: 183px;
    width: 361px; height: 43px;
    background: linear-gradient(90deg, var(--yellow), var(--yellow-deep));
    font-size: 13px;
    color: var(--ink);
    padding-left: 31px;
    line-height: 43px;
  }
  .name-plate {
    position: absolute;
    left: 374px; top: 183px;
    width: 172px; height: 43px;
    background: var(--slate);
    color: #ffffff;
    font-family: "Oswald", "Arial Narrow", sans-serif;
    font-weight: 600;
    font-size: 17px;
    text-transform: uppercase;
    line-height: 43px;
    text-align: center;
  }

  /* backs */
  .card--white .brand-mark,
  .card--slate .brand-mark,
  .card--umber .brand-mark { left: 221px; top: 38px; }
  .card--white .brand-name,
  .card--slate .brand-name,
  .card--umber .brand-name {
    left: 0; right: 0; text-align: center;
    top: 140px; font-size: 34px;
  }

  .option-label {
    position: absolute;
    color: var(--label);
    font-size: 21px;
    white-space: nowrap;
  }
  .option-label--2 { left: 999px; top: 19px; }
  .option-label--1 { left: 438px; top: 563px; }
  .option-label--3 { left: 995px; top: 573px; }
</style>
</head>
<body>
  <section class="card card--front">
    <div class="brand-mark"></div>
    <div class="brand-name">Vela Stewardship</div>
    <div class="contact">
      <div class="contact-line">0458 317 642</div>
      <div class="contact-line">mara@velastewardship.com.au</div>
      <div class="contact-line">www.velastewardship.com.au</div>
    </div>
    <div class="watermark-square"></div>
    <div class="address-band">214/53 Penrose Street, South Melbourne 3206</div>
    <div class="name-plate">Mara Dobrinsky</div>
  </section>

  <section class="card card--white">
    <div class="brand-mark"></div>
    <div class="brand-name">Vela Stewardship</div>
  </section>

  <section class="card card--slate">
    <div class="brand-mark"></div>
    <div class="brand-name">Vela Stewardship</div>
  </section>

  <section class="card card--umber">
    <div class="brand-mark"></div>
    <div class="brand-name">Vela Stewardship</div>
  </section>

  <div class="option-label option-label--2">back option 2</div>
  <div class="option-label option-label--1">back option 1</div>
  <div class="option-label option-label--3">back option 3</div>
</body>
</html>
```